Tallowick Limited Business Card

We need a business card for a new company based in Essex, United Kingdom. We develop and manufacture educational games. The business card needs to match the company brand and logo and the colour scheme.
My company makes educational board games to be played by the family or used by teachers
The games are tile based number game

Target Market(s)

Parents, teachers, schools and children

Industry/Entity Type

Games

Contact Information for Business Card

Company Name - Tallowick Limited
Director - Damian Prouse
Registered Office - 3 Marsh Court, 142 Quarry Lane, Brindleford, Essex, CM7 4XR
Phone Number - 07950 000 318
Email - Enquiries@Tallowick.example
Website - www.Tallowick.example
Company Number - 00000000

Font styles to use
Sans Serif

Colors
00a990
ffffff

Requirements
Must have
• Same colour scheme as the attachments - green and white
• Same font style for Tallowick
• Images of the number tiles similar to the attachments
• extra details
• The colour is Cyan - 82 Magenta - 24 Yellow - 44 Black - 2
• I have attached some of the font styles use on my website and alos my LOGO
Nice to have
• Image of the number "1" tag as seen on the website

```html
<!DOCTYPE html>
<html lang="en">
<head>
<meta charset="utf-8">
<title>Tallowick Limited Business Card</title>
<link rel="stylesheet" href="https://fonts.googleapis.com/css2?family=Open+Sans:wght@400;600;800&display=swap">
<style>
  :root {
    --teal: #1a9796;
    --teal-dark: #17898a;
    --green: #22b096;
    --white: #ffffff;
    --backdrop: #e6eaea;
  }
  * { box-sizing: border-box; margin: 0; padding: 0; }
  html, body { width: 1200px; height: 896px; overflow: hidden; }
  body {
    background: var(--backdrop);
    font-family: "Open Sans", Arial, sans-serif;
    position: relative;
  }
  .card {
    position: absolute;
    left: 280px;
    width: 640px;
    height: 366px;
    border-radius: 22px;
    overflow: hidden;
    box-shadow: 0 10px 28px rgba(0,0,0,0.18);
  }
  .card-front { top: 48px; background: var(--teal); }
  .card-back { top: 474px; background: var(--white); }

  /* front */
  .front-brand {
    position: absolute; left: 0; right: 0; top: 118px;
    text-align: center; color: var(--white);
  }
  .brand-name {
    font-weight: 800; font-size: 74px; line-height: 1; letter-spacing: -2px;
  }
  .brand-tagline {
    font-weight: 400; font-size: 21px; letter-spacing: 0.5px; margin-top: 6px;
  }

  /* back */
  .back-brand { position: absolute; left: 30px; top: 34px; color: var(--teal); }
  .back-brand .brand-name { font-size: 46px; letter-spacing: -1.3px; }
  .back-brand .brand-tagline { font-size: 13px; margin-top: 2px; letter-spacing: 0.2px; }

  .person {
    position: absolute; right: 30px; top: 36px; text-align: right; color: var(--teal);
    width: 330px; border-bottom: 2px solid var(--teal); padding-bottom: 6px;
  }
  .person-name { font-weight: 600; font-size: 30px; line-height: 1; letter-spacing: 0.2px; }
  .person-role { font-size: 14px; margin-top: 4px; }

  .address {
    position: absolute; right: 30px; top: 152px; text-align: right;
    color: var(--green); font-size: 15px; line-height: 1.4;
  }

  .contact {
    position: absolute; left: 30px; top: 196px; width: 290px;
    border-top: 2px solid var(--teal); padding-top: 10px;
    list-style: none; color: var(--green); font-size: 15px; line-height: 1.55;
  }
  .contact li { display: flex; align-items: center; gap: 10px; }
  .contact svg { width: 12px; height: 12px; flex: none; }

  .band {
    position: absolute; left: 0; right: 0; bottom: 0; height: 56px; display: flex;
  }
  .band-main { flex: 1; background: var(--green); }
  .band-gap { width: 4px; background: var(--white); }
  .band-number {
    width: 264px; background: var(--teal-dark); color: var(--white);
    font-size: 14px; display: flex; align-items: center; justify-content: center;
    letter-spacing: 0.3px; margin-top: -16px; position: relative;
  }
</style>
</head>
<body>
  <section class="card card-front" aria-label="Card front">
    <div class="front-brand">
      <div class="brand-name">Tallowick</div>
      <div class="brand-tagline">QUICK TILE COUNTING PLAY</div>
    </div>
  </section>

  <section class="card card-back" aria-label="Card back">
    <div class="back-brand">
      <div class="brand-name">Tallowick</div>
      <div class="brand-tagline">QUICK TILE COUNTING PLAY</div>
    </div>

    <div class="person">
      <div class="person-name">DAMIAN PROUSE</div>
      <div class="person-role">Director</div>
    </div>

    <p class="address">3 Marsh Court, 142 Quarry Lane,<br>Brindleford, Essex, CM7 4XR</p>

    <ul class="contact">
      <li>
        <svg viewBox="0 0 12 12" aria-hidden="true"><path d="M2.5 1 L4.5 1 L5 3.5 L3.8 4.5 Q5 7 7.5 8.2 L8.5 7 L11 7.5 L11 9.5 Q11 11 9.5 11 Q1 10 1 2.5 Q1 1 2.5 1Z" fill="var(--teal)"/></svg>
        07950 000 318
      </li>
      <li>
        <svg viewBox="0 0 12 12" aria-hidden="true"><rect x="0.8" y="2" width="10.4" height="8" rx="1" fill="none" stroke="var(--teal)" stroke-width="1.4"/><path d="M1 2.5 L6 6.5 L11 2.5" fill="none" stroke="var(--teal)" stroke-width="1.4"/></svg>
        Enquiries@Tallowick.example
      </li>
      <li>
        <svg viewBox="0 0 12 12" aria-hidden="true"><circle cx="6" cy="6" r="5" fill="none" stroke="var(--teal)" stroke-width="1.3"/><path d="M1 6 H11 M6 1 Q3 6 6 11 Q9 6 6 1" fill="none" stroke="var(--teal)" stroke-width="1"/></svg>
        www.Tallowick.example
      </li>
    </ul>

    <div class="band">
      <div class="band-main"></div>
      <div class="band-gap"></div>
      <div class="band-number">Company Number - 00000000</div>
    </div>
  </section>
</body>
</html>
```